Web Button design and production

I need remote control like buttons (or your own design of buttons if I like it)
3x4 text buttons (normal, pressed, disabled)
3x1 empty button (normal, pressed, disabled)
3x6 buttons with glyph (normal, pressed, disabled)
3x288 with 24h time "00:00", "00:05", "00:10" (normal, pressed, disabled)
4 LED (red, green, orange, black)
I will upload the background image as soon as possible (black plastic)
See attached images
Q: Do the buttons have to be gray/black?
A: It should look like a high end remote control. It could be brushed aluminum as well, or something you come up with. But I guess black or dark grey would be best. The background will be pixelvaultimages 40631758, but it's not available yet.
Q: Do I have to provide all buttons for the contest?
A: No! I only need one button (3 states) and a LED to decide. Only the winner will do the whole job.
Q: Is the Designer who wins the contest expected to complete all the extra buttons?
A: Yes, please.
Plastic

```html
<!DOCTYPE html>
<html lang="en">
<head>
<meta charset="utf-8">
<title>Remote Control Button Set</title>
<link rel="stylesheet" href="https://fonts.googleapis.com/css2?family=Arimo&family=Nothing+You+Could+Do&display=swap">
<style>
:root{
  --bg:#1d1d1d;
  --bg-grain:#222;
  --divider:#3a3a3a;
  --btn-top:#585858;
  --btn-bottom:#434343;
  --btn-hover-top:#626262;
  --btn-hover-bottom:#4b4b4b;
  --btn-active:#414141;
  --btn-border:#282828;
  --btn-edge:#2a2a2a;
  --btn-text:#f2f2f2;
  --red:#f2737a;
  --red-top:#f7868c;
  --red-edge:#c4434b;
  --red-glyph:#c9373f;
  --green:#a8cf62;
  --green-top:#b8da76;
  --green-edge:#7da23b;
  --green-glyph:#6c9130;
  --blue:#7fd2f4;
  --blue-top:#98dcf8;
  --blue-edge:#4aa5cf;
  --blue-glyph:#3b84a9;
  --heading:#f5f5f5;
}
*{margin:0;padding:0;box-sizing:border-box}
html,body{width:1200px;height:540px;overflow:hidden}
body{
  position:relative;
  background:
    repeating-linear-gradient(45deg,rgba(255,255,255,.018) 0 1px,transparent 1px 3px),
    repeating-linear-gradient(-45deg,rgba(0,0,0,.12) 0 1px,transparent 1px 3px),
    var(--bg);
  font-family:"Arimo",Arial,sans-serif;
}
.divider{position:absolute;top:6px;height:522px;border-left:1px dotted var(--divider)}
.state-heading{
  position:absolute;top:12px;width:160px;margin-left:-80px;text-align:center;
  font-family:"Nothing You Could Do",cursive;font-size:27px;color:var(--heading);letter-spacing:1px;
}
.btn{
  position:absolute;display:flex;align-items:center;justify-content:center;text-align:center;
  color:var(--btn-text);border:1px solid var(--btn-border);border-radius:5px;
  background:linear-gradient(var(--btn-top),var(--btn-bottom));
  box-shadow:inset 0 1px 0 rgba(255,255,255,.12),0 3px 0 var(--btn-edge),0 4px 3px rgba(0,0,0,.45);
}
.btn.is-hover{background:linear-gradient(var(--btn-hover-top),var(--btn-hover-bottom))}
.btn.is-active{background:var(--btn-active);box-shadow:inset 0 1px 2px rgba(0,0,0,.3),0 1px 1px rgba(0,0,0,.5)}
.btn-login{width:95px;height:53px;font-size:22px}
.btn-time{width:95px;height:53px;font-size:28px}
.btn-book{width:143px;height:92px;font-size:28px;line-height:1.18}
.led{position:absolute;width:47px;height:47px;border-radius:5px}
.led-red{background:linear-gradient(var(--red-top),var(--red));box-shadow:0 3px 0 var(--red-edge),0 4px 3px rgba(0,0,0,.45)}
.led-green{background:linear-gradient(var(--green-top),var(--green));box-shadow:0 3px 0 var(--green-edge),0 4px 3px rgba(0,0,0,.45)}
.led-blue{background:linear-gradient(var(--blue-top),var(--blue));box-shadow:0 3px 0 var(--blue-edge),0 4px 3px rgba(0,0,0,.45)}
.led.is-hover{filter:brightness(1.04)}
.led.is-active{box-shadow:0 1px 1px rgba(0,0,0,.5)}
.led-red.is-active{background:var(--red)}
.led-green.is-active{background:var(--green)}
.led-blue.is-active{background:var(--blue)}
.led.glyph{display:flex;align-items:center;justify-content:center}
.btn svg,.led svg{display:block}
</style>
</head>
<body>
<div class="divider" style="left:342px"></div>
<div class="divider" style="left:522px"></div>
<div class="divider" style="left:728px"></div>

<h2 class="state-heading" style="left:248px">LINK</h2>
<h2 class="state-heading" style="left:428px">HOVER</h2>
<h2 class="state-heading" style="left:606px">ACTIVE</h2>

<!-- Link state -->
<div class="btn btn-login" style="left:200px;top:60px">Login</div>
<div class="btn btn-time" style="left:200px;top:139px">00:00</div>
<div class="btn btn-book" style="left:179px;top:218px">Book<br>Now</div>
<div class="led led-red" style="left:224px;top:329px"></div>
<div class="led led-green" style="left:224px;top:397px"></div>
<div class="led led-blue" style="left:224px;top:470px"></div>

<!-- Hover state -->
<div class="btn btn-login is-hover" style="left:380px;top:60px">Login</div>
<div class="btn btn-time is-hover" style="left:380px;top:139px">00:00</div>
<div class="btn btn-book is-hover" style="left:361px;top:218px">Book<br>Now</div>
<div class="led led-red is-hover" style="left:404px;top:329px"></div>
<div class="led led-green is-hover" style="left:404px;top:397px"></div>
<div class="led led-blue is-hover" style="left:404px;top:470px"></div>

<!-- Active state -->
<div class="btn btn-login is-active" style="left:558px;top:62px">Login</div>
<div class="btn btn-time is-active" style="left:558px;top:141px">00:00</div>
<div class="btn btn-book is-active" style="left:539px;top:220px">Book<br>Now</div>
<div class="led led-red is-active" style="left:584px;top:331px"></div>
<div class="led led-green is-active" style="left:584px;top:399px"></div>
<div class="led led-blue is-active" style="left:584px;top:472px"></div>

<!-- Glyph buttons -->
<div class="btn" style="left:778px;top:36px;width:95px;height:53px" aria-label="Back">
  <svg width="36" height="22" viewBox="0 0 36 22"><path d="M0 11 L13 0 V7 H36 V15 H13 V22 Z" fill="#fff"/></svg>
</div>
<div class="btn" style="left:899px;top:36px;width:95px;height:53px" aria-label="Return">
  <svg width="30" height="24" viewBox="0 0 30 24"><path d="M0 17 L10 8 V13 H18 V0 H26 V20 H10 V26 Z" fill="#fff" transform="translate(2,-2)"/></svg>
</div>
<div class="btn" style="left:778px;top:109px;width:96px;height:92px" aria-label="Previous">
  <svg width="26" height="28" viewBox="0 0 26 28"><path d="M0 14 L26 0 V28 Z" fill="#fff"/></svg>
</div>
<div class="btn" style="left:900px;top:109px;width:96px;height:92px" aria-label="Next">
  <svg width="26" height="28" viewBox="0 0 26 28"><path d="M26 14 L0 0 V28 Z" fill="#fff"/></svg>
</div>
<div class="btn" style="left:778px;top:221px;width:96px;height:54px" aria-label="Skip back">
  <svg width="30" height="20" viewBox="0 0 30 20"><rect x="0" y="0" width="5" height="20" fill="#fff"/><path d="M7 10 L30 0 V20 Z" fill="#fff"/></svg>
</div>
<div class="btn" style="left:900px;top:221px;width:96px;height:54px" aria-label="Skip forward">
  <svg width="30" height="20" viewBox="0 0 30 20"><path d="M23 10 L0 0 V20 Z" fill="#fff"/><rect x="25" y="0" width="5" height="20" fill="#fff"/></svg>
</div>

<div class="led led-red glyph" style="left:778px;top:299px;width:48px;height:47px" aria-label="Power">
  <svg width="24" height="24" viewBox="0 0 24 24"><path d="M7 6 A9 9 0 1 0 17 6" fill="none" stroke="var(--red-glyph)" stroke-width="2.4" stroke-linecap="round"/><line x1="12" y1="2" x2="12" y2="12" stroke="var(--red-glyph)" stroke-width="2.4" stroke-linecap="round"/></svg>
</div>
<div class="led led-red glyph" style="left:834px;top:299px;width:48px;height:47px" aria-label="Record">
  <svg width="22" height="22" viewBox="0 0 22 22"><circle cx="11" cy="11" r="10" fill="var(--red-glyph)"/></svg>
</div>
<div class="led led-green glyph" style="left:890px;top:299px;width:48px;height:47px" aria-label="Down">
  <svg width="26" height="24" viewBox="0 0 26 24"><path d="M2 2 L13 22 L24 2" fill="none" stroke="var(--green-glyph)" stroke-width="2.6"/></svg>
</div>
<div class="led led-green glyph" style="left:948px;top:299px;width:48px;height:47px" aria-label="Up">
  <svg width="26" height="24" viewBox="0 0 26 24"><path d="M2 22 L13 2 L24 22" fill="none" stroke="var(--green-glyph)" stroke-width="2.6"/></svg>
</div>

<div class="led led-blue glyph" style="left:778px;top:371px;width:68px;height:44px" aria-label="Rewind">
  <svg width="30" height="14" viewBox="0 0 30 14"><path d="M0 7 L15 0 V14 Z M15 7 L30 0 V14 Z" fill="var(--blue-glyph)"/></svg>
</div>
<div class="btn" style="left:865px;top:371px;width:47px;height:44px" aria-label="Play">
  <svg width="18" height="18" viewBox="0 0 18 18"><path d="M18 9 L0 0 V18 Z" fill="#fff"/></svg>
</div>
<div class="led led-blue glyph" style="left:926px;top:371px;width:69px;height:44px" aria-label="Fast forward">
  <svg width="30" height="14" viewBox="0 0 30 14"><path d="M15 7 L0 0 V14 Z M30 7 L15 0 V14 Z" fill="var(--blue-glyph)"/></svg>
</div>

<div class="btn" style="left:778px;top:445px;width:48px;height:44px" aria-label="Stop">
  <svg width="15" height="15" viewBox="0 0 15 15"><rect width="15" height="15" rx="2" fill="#fff"/></svg>
</div>
<div class="btn" style="left:835px;top:445px;width:70px;height:44px" aria-label="Pause or play">
  <svg width="46" height="20" viewBox="0 0 46 20"><rect x="0" y="0" width="5" height="20" fill="#fff"/><rect x="8" y="0" width="5" height="20" fill="#fff"/><line x1="15" y1="20" x2="22" y2="0" stroke="#fff" stroke-width="2.4"/><path d="M46 10 L25 0 V20 Z" fill="#fff"/></svg>
</div>
</body>
</html>
```